Graduation Day Sale Banner Ad for Website

We need a banner for our upscale jewelry website. Banner must have a classy high end look. The size of the banner must be 1187 × 400. I have attached pieces we would like used (some or all). The banner is for a Graduation Day sale that we are running. The banner should say "Graduation Day Gifts on Sale"

Target Market(s)

Wealthy individuals looking to buy graduation gifts for their children

Industry/Entity Type

Jewelry

Requirements
Must have
• Must match the look and feel of the website (www.velmira-studio.com)

```html
<!DOCTYPE html>
<html lang="en">
<head>
<meta charset="utf-8">
<title>Graduation Day Gifts on Sale – Banner</title>
<link href="https://fonts.googleapis.com/css2?family=Italianno&family=Montserrat:wght@400&display=swap" rel="stylesheet">
<style>
  :root {
    --page-bg: #f2f2f2;
    --sky: #a9d3da;
    --mist: #e6ede6;
    --sand: #f0d9a8;
    --gold-light: #f7e39a;
    --gold: #d9b04d;
    --gold-deep: #b98a2e;
    --ring-brown: #3b2a20;
    --seal-white: #ffffff;
    --headline: #545454;
    --caps-text: #4a3a30;
  }
  * { margin: 0; padding: 0; box-sizing: border-box; }
  html, body {
    width: 1200px; height: 1200px; overflow: hidden;
    background: var(--page-bg);
  }
  .banner {
    position: absolute;
    left: 125px; top: 440px;
    width: 950px; height: 320px;
    background: linear-gradient(180deg, var(--sky) 0%, var(--mist) 55%, var(--sand) 100%);
    overflow: hidden;
  }
  .seal {
    position: absolute;
    left: 48px; top: 16px;
    width: 212px; height: 290px;
  }
  .brand-name {
    font-family: "Italianno", cursive;
    font-size: 34px;
    fill: var(--ring-brown);
  }
  .seal-caps {
    font-family: "Montserrat", sans-serif;
    font-size: 13px;
    letter-spacing: 2.5px;
    fill: var(--caps-text);
  }
  .product-photo {
    position: absolute;
    left: 406px; top: 92px;
    width: 324px; height: 106px;
    border-radius: 40px;
    background: radial-gradient(ellipse at center, #e8c46a 0%, #d8b25a 40%, rgba(230,225,205,0.2) 75%, rgba(230,225,205,0) 100%);
  }
  .headline {
    position: absolute;
    left: 250px; top: 212px;
    width: 650px;
    text-align: center;
    font-family: "Italianno", cursive;
    font-weight: 400;
    font-size: 74px;
    line-height: 1;
    word-spacing: 10px;
    color: var(--headline);
    white-space: nowrap;
  }
</style>
</head>
<body>
  <section class="banner">
    <svg class="seal" viewBox="0 0 212 290">
      <defs>
        <linearGradient id="goldFace" x1="0" y1="0" x2="1" y2="1">
          <stop offset="0" stop-color="#f7e39a"/>
          <stop offset="0.5" stop-color="#d9b04d"/>
          <stop offset="1" stop-color="#b98a2e"/>
        </linearGradient>
        <linearGradient id="ribbonFace" x1="0" y1="0" x2="0" y2="1">
          <stop offset="0" stop-color="#d9b04d"/>
          <stop offset="1" stop-color="#f7e39a"/>
        </linearGradient>
        <path id="arcTop" d="M 40 106 A 66 66 0 0 1 172 106"/>
        <path id="arcBottom" d="M 44 122 A 64 64 0 0 0 168 122"/>
      </defs>
      <path class="seal-ribbon" d="M 61 200 L 151 200 L 151 284 L 106 262 L 61 284 Z" fill="url(#ribbonFace)"/>
      <path d="M 68 206 L 68 274 L 106 255 L 144 274 L 144 206" fill="none" stroke="#3b2a20" stroke-width="1.2" stroke-dasharray="4 3"/>
      <circle cx="106" cy="106" r="104" fill="url(#goldFace)"/>
      <circle cx="106" cy="106" r="93" fill="#3b2a20"/>
      <circle cx="106" cy="106" r="88" fill="#ffffff"/>
      <text class="seal-caps"><textPath href="#arcTop" startOffset="50%" text-anchor="middle">SPECIAL OFFER</textPath></text>
      <text class="seal-caps"><textPath href="#arcBottom" startOffset="50%" text-anchor="middle">GUARANTEED</textPath></text>
      <text class="brand-name" x="106" y="116" text-anchor="middle" textLength="128" lengthAdjust="spacingAndGlyphs">Velmira Studio</text>
    </svg>

    <div class="product-photo" role="img" aria-label="Three gold rings: a rolling three-band ring, a pearl and diamond crossover ring, and a two-tone gold band"></div>

    <h1 class="headline">Graduation Day Gifts on Sale</h1>
  </section>
</body>
</html>
```